Brennick Setter Club - Rare dog breed club needs web design!

The Transylvanian Hound (or Erdélyi kopó) is an ancient Hungarian dog breed. These medium-sized hounds were favored by the Hungarian kings and princes for hunting bears and wolves in the Carpathian mountains of Transylvania. The breed's great adaptability to the region's extreme climates of sweltering summers and frigid winters made it an excellent all season hunting dog. This dog has a sleek appearance and stunning good looks. They are lean, appear very elegant and proud. Their erect posture and beautifully sculpted head portray great attentiveness and authority. In general, this rare breed is extremely good natured, loyal and obedient. It has a tendency to form strong attachments to its primary caretakers and will remain loyal and protective. (Please refer to existing web resources.)

The Brennick Setter Club - with current website www.brennicksetter.com - is the official breed club of Transylvanian Hound afficionados, breeders and owners in the United States, which was founded in 2010. We are looking for a web design for the new, upgraded version of this central (currenty non-functioning) website. Please do not recycle the old logo (we may choose from your suggesions and pay for it!) or any of the old texts. Please use the structure described below. Overall, the webpage serves a dual purpose: an educational one (about the breed itself) and a community-building one (inside the Club). The proposed structure of the website is as follows:

1. About the Kopó
- Breed History
- Breed Standard
- Public Education
- Photo Gallery

2. Life with a Kopó
- Health and Genetics
- Feeding and Nutrition
- Training and Activities

3. Finding a Kopó
- Is this the Right Breed for You?
- Choosing a Puppy
- FAQ
- Breeder Referral

4. The Brennick Setter Club
- Constituton
- Officers and Appointees
- Code of Ethics
- Breeder Guidelines
- Membership
- Reports
- Links

5. News and Events

6. Shop

We are attaching a couple of examples of the graphics/drawings of the dogs that would be part of the design of the website. We plan to have more of these artistic depictions, nicely embedded into the background (maybe shaded out at the edges just like the drawings themselves) and less actual photos. Or a good combination of the two.

Further information upon request.

Reason: There are a few very promising design collaborations ongoing. As we moved the brief to a more artistic and graphic direction, we felt that one week of extension would be needed to get to the perfect end-product, which could include designs for sub-pages as well.

Reason: In order to make the final modifications to the leading designs, and at the request of those designers, the deadline is extended until Friday.

Target Market(s)

- BRSC Club members, dog (especially T-Hound) owners, past and future owners, breeders, puppy buyers, hunters, kennel clubs, dog show participants, vets, animal shelters, Hungarian, Romanian and other European web visitors, historians

Industry/Entity Type

Club

Font styles to use
Serif
Decorative
Script

Requirements
Must have
• - Sync with graphics of dogs (see attachments), but accentuate the rich black basic color of the dogs
- Elegance, aristocratic/noble look and feel (but not overly archaic)
- Love, companionship, dogs as family members
- Hunting usage, but no bloody associations, rather romantic ones
- Simple to use and navigate for non-web-natives
- Old world (Central European) atmosphere, even the exotic, rustic and romantic Transylvanian feel - SEE the new attachment for inspiration (this was a design plan which we discarded (mainly because of its gothic, (nazi-like), unreadable font, and the fact that the plan makes the black-looking dogs appear brown), however we loved the fact that it was not full of boxes/windows, had a marble/sand stone like continuous background, lots of little elegant graphics, the drawings embedded, etc.
Nice to have
• - Working on smartphone, Zentabs, etc., so dynamic website design
- Web shop to be added to functionalities in the future (?)
- English language for now, in the future can be Hungarian, Romanian, etc., so the font choice should handle various alphabets
- Focus on the dogs (likely more graphics than photos, at least on the main pages), and not on the activities/humans - the design should accentuate the black and not the tan of the graphics!
Should not have
• - Old logo from the old www.brennicksetter.com webpage or the other logo from the Chatterly site of the Brennick Setter Club, we will have a new one (maybe designed by you!)
- Breed club, kennel club cliches
- Cutesy, adorable, cheesy design elements
- Old, stale, monolithic, archaic, snobbish, etc. look and feel
- No vampire associations

```html
<!DOCTYPE html>
<html lang="en">
<head>
<meta charset="utf-8">
<title>Brennick Setter Club</title>
<link href="https://fonts.googleapis.com/css2?family=Alegreya:wght@400;700&family=Ubuntu:wght@400;700&display=swap" rel="stylesheet">
<style>
:root{
  --wood-dark:#3a2214;
  --wood-mid:#5a3620;
  --wood-light:#6e4428;
  --parch-light:#f6c56e;
  --parch-mid:#e9a94c;
  --parch-edge:#c98431;
  --ink:#2b1608;
  --brown:#6e3212;
  --brown-soft:#8a4a1e;
  --red-pill:#a63a1c;
  --nav-small:#8a4d1c;
  --gold:#c9a13a;
  --badge:#d9ad74;
  --badge-edge:#a77646;
  --icon:#231510;
  --date-bg:#2b1a10;
  --date-fg:#f3d08a;
}
*{box-sizing:border-box;margin:0;padding:0}
html,body{width:1081px;height:1200px;overflow:hidden}
body{
  position:relative;
  font-family:"Ubuntu",sans-serif;
  color:var(--ink);
  background:
    repeating-linear-gradient(90deg,rgba(0,0,0,0) 0 118px,rgba(0,0,0,.35) 118px 121px,rgba(0,0,0,0) 121px 240px),
    repeating-linear-gradient(90deg,var(--wood-mid) 0 30px,var(--wood-light) 30px 55px,var(--wood-dark) 55px 90px,var(--wood-mid) 90px 121px);
}
.abs{position:absolute}
.parchment{
  left:106px;top:110px;width:868px;height:930px;
  background:radial-gradient(ellipse at 40% 45%,var(--parch-light) 0%,var(--parch-mid) 70%,var(--parch-edge) 100%);
  box-shadow:0 0 18px rgba(0,0,0,.5);
}
.roll{
  background:linear-gradient(180deg,var(--parch-light),var(--parch-mid) 60%,var(--parch-edge));
  box-shadow:0 6px 14px rgba(0,0,0,.45);
}
.roll-top{left:104px;top:24px;width:892px;height:118px;border-radius:10px 30px 10px 10px}
.roll-bottom{left:102px;top:1016px;width:894px;height:130px;border-radius:30px 10px 14px 14px}
.wordmark{font-family:"Alegreya",serif;font-weight:700;color:var(--brown);font-size:27px;line-height:31px;letter-spacing:1px}
.wordmark.top{left:126px;top:40px}
.wordmark.foot{left:756px;top:1048px;font-size:23px;line-height:27px}
.util-nav{left:457px;top:37px;display:flex;gap:15px;font-size:9.5px;color:var(--nav-small);align-items:center;white-space:nowrap}
.util-nav .dot{display:inline-block;width:14px;height:14px;border-radius:50%;background:#3b5d9c;vertical-align:middle;margin-right:3px}
.main-nav{left:437px;top:64px;display:flex;gap:31px;font-family:"Alegreya",serif;font-size:17px;color:var(--ink);align-items:center}
.main-nav .current{background:var(--red-pill);color:#f6d9b0;padding:2px 14px;border-radius:4px}
.phone{left:760px;top:128px;font-family:"Alegreya",serif;font-size:21px;font-weight:700;color:#f4dcae;text-shadow:0 1px 2px rgba(0,0,0,.5);display:flex;align-items:center;gap:6px}
.hero-frame{left:132px;top:160px;width:822px;height:299px;border:4px solid var(--gold);padding:10px;background:#b98a37;box-shadow:inset 0 0 0 3px #7d5a1c}
.hero-photo{width:100%;height:100%;
  background:
    linear-gradient(90deg,rgba(60,30,40,.35),rgba(60,30,40,0) 30%,rgba(60,30,40,0) 70%,rgba(60,30,40,.35)),
    linear-gradient(180deg,#a8a060 0%,#6a6a34 22%,#4a3a3e 45%,#3c2f3c 65%,#4c4a32 82%,#3e3c26 100%)}
.portrait{left:130px;top:479px;width:167px;height:176px;border-radius:40% 40% 46% 46%;border:3px solid #5a2a10;box-shadow:0 0 0 2px #c98a44;
  background:radial-gradient(ellipse at 50% 58%,#2a1c14 0%,#3a2418 38%,#8a5a30 62%,#c49060 100%)}
.welcome{left:312px;top:476px;width:638px}
.h-section{font-family:"Alegreya",serif;font-weight:400;color:var(--brown);font-size:27px}
.welcome .h-section{border-bottom:1px solid var(--brown-soft);width:341px;padding-bottom:2px}
.welcome h2{font-size:15px;font-weight:700;margin-top:12px;line-height:15px}
.welcome p{font-size:10.5px;line-height:13px;text-align:justify;margin-bottom:7px}
.welcome p.first{margin-bottom:12px}
.news-glow{left:650px;top:660px;width:330px;height:340px;border-radius:50%;background:radial-gradient(circle,rgba(196,110,40,.45),rgba(196,110,40,0) 70%)}
.news-title{left:704px;top:684px}
.all-btn{left:889px;top:697px;width:61px;height:22px;background:var(--date-bg);color:#f3b04a;font-size:9px;font-weight:700;text-align:center;line-height:22px;border-bottom:2px solid #e0761e}
.news-item{left:704px;display:flex;gap:14px;width:250px}
.news-thumb{width:90px;height:52px;flex:none}
.thumb-grass{background:linear-gradient(180deg,#9aa88a 0%,#6a7a4a 50%,#4a5a2a 100%)}
.thumb-rest{background:linear-gradient(180deg,#c8b8a8 0%,#6a4a38 55%,#8a6a50 100%)}
.news-body .date{display:inline-block;background:var(--date-bg);color:var(--date-fg);font-size:9px;font-weight:700;padding:1px 6px;margin-top:3px}
.news-body p{font-family:"Alegreya",serif;font-size:11px;line-height:15px;margin-top:2px}
.badge{top:697px;width:178px;height:140px;border-radius:36px;background:radial-gradient(circle,#f0d4a8,var(--badge) 70%,#b88752);border:3px solid var(--badge-edge);box-shadow:0 0 0 4px #e5b673,0 4px 8px rgba(0,0,0,.3);text-align:center}
.badge .icon{display:block;margin:14px auto 6px;height:50px}
.badge .icon-blob{width:44px;height:54px;margin:12px auto 4px;border-radius:45% 45% 30% 30%;background:radial-gradient(circle at 50% 40%,var(--icon),rgba(35,21,16,.75))}
.badge span{font-family:"Alegreya",serif;font-size:25px;color:#7a3018}
.col{top:850px;width:176px;text-align:center}
.col .h-section{font-size:22px;border-bottom:1px solid var(--brown-soft);padding-bottom:2px}
.col .thumb{width:120px;height:57px;margin:12px auto 0;border:2px solid #eee1c6;box-shadow:0 1px 3px rgba(0,0,0,.4)}
.col p{font-size:10.5px;line-height:16px;margin-top:9px;padding:0 4px}
.foot-nav{left:127px;top:1081px;display:flex;gap:36px;font-family:"Alegreya",serif;font-size:14px;color:var(--brown)}
.copy{left:127px;top:1111px;font-family:"Alegreya",serif;font-size:11.5px}
</style>
</head>
<body>
<div class="abs parchment"></div>
<div class="abs roll roll-top"></div>
<div class="abs roll roll-bottom"></div>

<header>
  <div class="abs wordmark top">BRENNICK SETTER<br>CLUB</div>
  <nav class="abs util-nav">
    <span>TRAINING</span><span>HEALTH</span><span>FIND A PUPPY</span><span>GALLERY</span>
    <span><i class="dot"></i>JOIN US ON CHATTERLY</span><span>NEWS AND EVENTS</span><span>FORUM</span>
  </nav>
  <nav class="abs main-nav">
    <span class="current">Home</span><span>History</span><span>Standards</span><span>Members</span><span>CKR Info</span><span>Contact</span>
  </nav>
  <div class="abs phone">
    <svg width="24" height="22" viewBox="0 0 24 22"><path d="M3 8c0-4 18-4 18 0l-1 3h-4l-1-3c-2-1-4-1-6 0L8 11H4z" fill="#f4dcae"/><rect x="5" y="13" width="14" height="8" rx="2" fill="#f4dcae"/></svg>
    0757-55501946
  </div>
</header>

<div class="abs hero-frame"><div class="hero-photo" role="img" aria-label="Club members and their hounds gathered outdoors"></div></div>

<div class="abs portrait" role="img" aria-label="Portrait of a black and tan hound in an ornate frame"></div>
<section class="abs welcome">
  <h1 class="h-section">Welcome</h1>
  <h2>BY BUILDING THIS WEBSITE, OUR AIM IS TO CREATE</h2>
  <p class="first">a virtual forum to everyone, who wish to know more about Transylvanian Hounds, and would like to join us in expanding their popularity and number in the US.</p>
  <p>It is really important to us to have the Transylvanian Hound registered with CKR, this way more and more people can be introduced to this historical breed. The breed registration is a long procedure, and we are inviting all Transylvanian Hound owners to register and sign up with us. This way, we can have the breed recognized by CKR quicker.</p>
  <p>Since this is a constantly developing website, we are greatly appreciate your advice, opinion, pictures, and stories that could help us create a well functioning interactive Brennick Setter Club.</p>
  <p>Thank you for joining us and please be a member of our Club.</p>
</section>

<div class="abs news-glow" role="img" aria-label="Faint drawing of a hound"></div>
<h2 class="abs h-section news-title">Latest news</h2>
<div class="abs all-btn">ALL</div>
<div class="abs news-item" style="top:724px"><div class="news-thumb thumb-grass" role="img" aria-label="Hound standing on grass"></div><div class="news-body"><span class="date">04/21/14</span><p>Suspendisse porta sit amet eros ut dapibus.</p></div></div>
<div class="abs news-item" style="top:792px"><div class="news-thumb thumb-rest" role="img" aria-label="Hound resting"></div><div class="news-body"><span class="date">04/21/14</span><p>Suspendisse porta sit amet eros ut dapibus.</p></div></div>
<div class="abs news-item" style="top:861px"><div class="news-thumb thumb-grass" role="img" aria-label="Hound standing on grass"></div><div class="news-body"><span class="date">04/21/14</span><p>Suspendisse porta sit amet eros ut dapibus.</p></div></div>
<div class="abs news-item" style="top:927px"><div class="news-thumb thumb-rest" role="img" aria-label="Hound resting"></div><div class="news-body"><span class="date">04/21/14</span><p>Suspendisse porta sit amet eros ut dapibus.</p></div></div>

<div class="abs badge" style="left:132px">
  <svg class="icon" width="80" height="50" viewBox="0 0 80 50" aria-label="Whistle icon" role="img">
    <circle cx="14" cy="14" r="8" fill="none" stroke="var(--icon)" stroke-width="4"/>
    <path d="M18 16h56v10H48c0 12-8 20-18 20s-18-8-18-20c0-5 2-8 6-10z" fill="var(--icon)"/>
  </svg>
  <span>Training</span>
</div>
<div class="abs badge" style="left:321px">
  <svg class="icon" width="96" height="50" viewBox="0 0 96 50" aria-label="Bone icon" role="img">
    <g fill="var(--icon)">
      <circle cx="14" cy="17" r="10"/><circle cx="14" cy="33" r="10"/>
      <circle cx="82" cy="17" r="10"/><circle cx="82" cy="33" r="10"/>
      <rect x="14" y="18" width="68" height="14" rx="5"/>
    </g>
  </svg>
  <span style="font-size:22px">Find a puppy</span>
</div>
<div class="abs badge" style="left:509px"><div class="icon-blob" role="img" aria-label="Sitting dog icon"></div><span style="font-size:23px">Gallery</span></div>

<section class="abs col" style="left:130px"><h3 class="h-section">About the club</h3><div class="thumb" role="img" aria-label="Hounds by the water" style="background:linear-gradient(180deg,#8a9aa8,#3a3a34 70%,#6a6a5a)"></div><p>By building this website, our aim is to create a virtual forum to everyone.</p></section>
<section class="abs col" style="left:322px"><h3 class="h-section">Standards</h3><div class="thumb" role="img" aria-label="Close view of a hound" style="background:radial-gradient(ellipse at 50% 70%,#1e140e,#4a3424 60%,#8a6a4a)"></div><p>By building this website, our aim is to create a virtual forum to everyone.</p></section>
<section class="abs col" style="left:520px;width:182px"><h3 class="h-section">Contact</h3><div class="thumb" role="img" aria-label="Puppies on grass" style="background:linear-gradient(180deg,#7a9a5a,#2a2a1a 55%,#4a6a2a)"></div><p>By building this website, our aim is to create a virtual forum to everyone.</p></section>

<footer>
  <nav class="abs foot-nav"><span>Home</span><span>History</span><span>Standards</span><span>Members</span><span>CKR Info</span><span>Contact</span></nav>
  <div class="abs copy">All rights reserved 2014</div>
  <div class="abs wordmark foot">BRENNICK SETTER<br>CLUB</div>
</footer>
</body>
</html>
```